Tarvell homes and renovations business card design.

Would like some new card designs utilizing my new logo that look professional. I am open to different colors on the logo or utilize the same ones we have. I like the original concept but would like to see some fresh ideas and build on what we have already done.

Target Market(s)

Custom home building industry, Real estate sales, Renovation projects.

Industry/Entity Type

Home Builder

Contact Information for Business Card

Tarvell Homes and Renovations
2871 162nd Street
Ashcombe, Northvale
T0L3P0
Home : 010- 555-0187 Cell: 010- 555-0243

My info is : Gus Tarvell, President and CEO
email: tarvellhomes@quillmail.example
Website: tarvellhomes.example

Requirements
Must have
• Must Use my new logo design. I am open to different colors on the logo or utilize the same ones in the existing design. I can upload the original logo design if needed.

```html
<!DOCTYPE html>
<html lang="en">
<head>
<meta charset="utf-8">
<title>Tarvell Homes and Renovations – Business Card</title>
<link href="https://fonts.googleapis.com/css2?family=Roboto+Condensed:wght@400;700&display=swap" rel="stylesheet">
<style>
  :root {
    --page-bg: #ffffff;
    --card-bg: #000000;
    --brand-gold: #c8952a;
    --brand-grey: #4a4a4a;
    --text-light: #ffffff;
  }
  html, body {
    margin: 0;
    padding: 0;
    width: 1200px;
    height: 1001px;
    overflow: hidden;
    background: var(--page-bg);
  }
  .canvas {
    position: relative;
    width: 1200px;
    height: 1001px;
    display: flex;
    justify-content: center;
    align-items: center;
    gap: 60px;
    font-family: "Roboto Condensed", "Arial Narrow", sans-serif;
  }
  .card {
    position: relative;
    width: 340px;
    height: 595px;
    background: var(--card-bg);
    color: var(--text-light);
    box-sizing: border-box;
    overflow: hidden;
  }
  .brand {
    position: absolute;
    top: 130px;
    left: 0;
    right: 0;
    display: flex;
    justify-content: center;
    align-items: center;
    gap: 8px;
  }
  .brand-mark {
    width: 12px;
    height: 12px;
    flex: none;
  }
  .brand-name {
    font-weight: 400;
    font-size: 19px;
    letter-spacing: 0.3px;
    text-transform: uppercase;
    white-space: nowrap;
    line-height: 1;
  }
  .card-front .brand-mark { background: var(--brand-gold); }
  .card-front .brand-name { color: var(--brand-gold); }
  .card-back .brand-mark { background: var(--brand-grey); }
  .card-back .brand-name { color: var(--brand-grey); }

  .holder {
    position: absolute;
    right: 36px;
    bottom: 62px;
    text-align: center;
  }
  .holder-name {
    font-weight: 700;
    font-size: 22px;
    margin: 0;
  }
  .holder-title {
    font-weight: 400;
    font-size: 22px;
    margin: 2px 0 0;
  }
  .contact {
    position: absolute;
    left: 0;
    right: 0;
    bottom: 58px;
    text-align: center;
    font-size: 16px;
    line-height: 1.4;
  }
  .contact p { margin: 0; white-space: nowrap; }
  .contact .address { margin-bottom: 10px; }
</style>
</head>
<body>
<main class="canvas">
  <section class="card card-front" aria-label="Business card front">
    <div class="brand">
      <span class="brand-mark"></span>
      <span class="brand-name">Tarvell Homes and Renovations</span>
    </div>
    <div class="holder">
      <p class="holder-name">Gus Tarvell</p>
      <p class="holder-title">President and CEO</p>
    </div>
  </section>

  <section class="card card-back" aria-label="Business card back">
    <div class="brand">
      <span class="brand-mark"></span>
      <span class="brand-name">Tarvell Homes and Renovations</span>
    </div>
    <div class="contact">
      <div class="address">
        <p>2871 162nd Street Ashcombe, Northvale,</p>
        <p>T0L3P0</p>
      </div>
      <p>Email: tarvellhomes@quillmail.example</p>
      <p>Website: tarvellhomes.example</p>
      <p>Home : 010- 555-0187 Cell: 010- 555-0243</p>
    </div>
  </section>
</main>
</body>
</html>
```